Recruitment #1

We are looking for an effective ad to recruit work from home Loan Officers for our Mortgage Brokerage.
Use the following text...
Earn Mortgage Income in your sleep. Its as easy as 1, 2, 3.....
1) Solicit Potential Applicants (Word of Mouth, Email, Social Media etc.)
2) Take Complete Applications & Submit Them
3) Wait to Get Paid.......(Avg. $2,500 per closing)
"You open the Bluegate, We'll handle the rest"
No Experience Necessary
No Goals or Quotas
No Office Hours / Work from Home Office
...and We Fully Reimburse ALL LICENSING FEES!!
Email Resume to mkowal@bluegatehomeloans.com
Bluegate Financial Services, Inc.
731 W Orchard Avenue, #318
Baltimore, MD 21417
NMLS #386147
www.bluegatehomeloans.com
Phone (800) 640-2915
Licensed Mortgage Broker in MD and DC since 1997
Professionals looking to earn part time income at Loan Officers, preferably with strong social media following.
Loan

```html
<!DOCTYPE html>
<html lang="en">
<head>
<meta charset="utf-8">
<title>Bluegate Financial Services – Loan Officer Recruitment</title>
<link rel="stylesheet" href="https://fonts.googleapis.com/css2?family=Roboto+Condensed:ital,wght@0,400;0,700;1,700&family=Lato:wght@400;700&family=Arimo:wght@400;700&display=swap">
<style>
  :root {
    --blue: #0b63b6;
    --blue-dark: #0a4f94;
    --gold: #b29a2a;
    --gold-light: #c9b43a;
    --ink: #222222;
    --text: #333333;
    --white: #ffffff;
    --page: #eeeeee;
    --line: #d8d8d8;
  }
  * { margin: 0; padding: 0; box-sizing: border-box; }
  html, body { width: 900px; height: 1200px; overflow: hidden; background: var(--page); }
  .canvas { position: relative; width: 900px; height: 1200px; }
  .flyer {
    position: absolute; left: 65px; top: 40px; width: 783px; height: 1105px;
    background: var(--white); overflow: hidden;
    box-shadow: 0 2px 8px rgba(0,0,0,.25);
    font-family: "Arimo", Arial, sans-serif;
  }
  .headline { position: absolute; left: 50px; top: 46px; font-family: "Roboto Condensed", "Arial Narrow", sans-serif; font-weight: 700; line-height: 1; }
  .headline span { display: block; }
  .headline .l1 { color: var(--blue); font-size: 41px; }
  .headline .l2 { color: var(--gold); font-size: 47px; margin-top: 8px; }
  .headline .l3 { color: var(--blue); font-size: 37px; margin-top: 9px; }

  .hero-photo {
    position: absolute; left: 305px; top: 0; width: 478px; height: 508px;
    background: radial-gradient(ellipse at 65% 45%, #e8d2c0 0%, #f3ebe3 45%, #ffffff 80%);
  }
  .brand { position: absolute; left: 32px; top: 350px; display: flex; align-items: center; gap: 12px; }
  .brand-dot { width: 22px; height: 22px; border-radius: 50%; background: var(--blue); }
  .brand-name { font-family: "Arimo", Arial, sans-serif; font-weight: 700; font-size: 17px; color: var(--blue); }

  .steps { position: absolute; left: 0; top: 508px; width: 783px; height: 146px; }
  .step { position: absolute; top: 0; height: 146px; color: var(--white); text-align: center; font-size: 15px; line-height: 19px; }
  .step.blue { background: linear-gradient(#1a74c7, var(--blue-dark)); }
  .step.gold { background: linear-gradient(var(--gold-light), #a88f22); }
  .step p { position: absolute; left: 0; right: 0; top: 68px; padding: 0 14px; }
  .step-num {
    position: absolute; top: -46px; width: 110px; height: 80px; border-radius: 50%;
    border: 5px solid var(--white); color: var(--white);
    font-family: "Roboto Condensed", sans-serif; font-weight: 700; font-size: 62px; line-height: 70px; text-align: center;
  }
  .step.blue .step-num { background: var(--blue); }
  .step.gold .step-num { background: var(--gold); }

  .family-photo {
    position: absolute; left: 0; top: 654px; width: 783px; height: 400px;
    background: linear-gradient(90deg, #ffffff 0%, #f1f1f1 30%, #e6e6e6 55%, #f4f4f4 85%, #ffffff 100%);
  }
  .tagline {
    position: absolute; left: 0; top: 695px; width: 480px; height: 34px;
    background: var(--gold); color: var(--white);
    clip-path: polygon(0 0, 100% 0, 96% 100%, 0 100%);
    font-family: "Roboto Condensed", sans-serif; font-style: italic; font-weight: 700; font-size: 17.5px; line-height: 34px; padding-left: 30px;
  }
  .perks { position: absolute; left: 32px; top: 744px; list-style: none; font-family: "Lato", sans-serif; font-size: 22px; color: var(--text); }
  .perks li { height: 32px; line-height: 32px; }
  .perks li::before { content: ""; display: inline-block; width: 7px; height: 7px; border-radius: 50%; background: var(--blue); margin-right: 10px; vertical-align: middle; position: relative; top: -3px; }
  .reimburse { position: absolute; left: 33px; top: 855px; font-family: "Roboto Condensed", sans-serif; font-weight: 700; line-height: 1; }
  .reimburse .r1 { display: block; font-size: 29px; color: var(--ink); }
  .reimburse .r2 { display: block; font-size: 37px; color: var(--blue); margin-top: 6px; }

  .money-bag {
    position: absolute; left: 25px; top: 930px; width: 210px; height: 175px;
    background: radial-gradient(ellipse at 50% 60%, #b99c6c 0%, #d6c3a0 45%, rgba(255,255,255,0) 72%);
  }
  .footer-band { position: absolute; left: 0; top: 1053px; width: 783px; height: 52px; background: linear-gradient(var(--gold-light), #ae9626); }
  .web {
    position: absolute; left: 430px; top: 1003px; width: 353px; height: 66px;
    background: linear-gradient(#1a74c7, var(--blue-dark)); clip-path: polygon(4% 0, 100% 0, 100% 100%, 0 100%);
    color: var(--white); font-size: 16px; font-weight: 700; letter-spacing: 2.4px; line-height: 66px; padding-left: 40px;
  }

  .resume {
    position: absolute; left: 500px; top: 687px; width: 300px; height: 61px;
    border: 3px solid var(--blue); border-right: none; border-radius: 22px 0 0 22px; background: var(--white);
    font-family: "Lato", sans-serif; text-align: center; padding-right: 20px;
  }
  .resume .label { display: block; font-weight: 700; font-size: 22px; color: var(--ink); margin-top: 5px; }
  .resume .email { display: block; font-weight: 700; font-size: 13.5px; color: var(--ink); }
  .contact { position: absolute; left: 523px; top: 768px; color: var(--ink); }
  .contact .call { font-weight: 700; font-size: 15px; }
  .contact .phone { font-family: "Roboto Condensed", sans-serif; font-weight: 700; font-size: 34px; color: var(--gold); line-height: 1; margin-top: 5px; }
  .rule { position: absolute; left: 515px; width: 255px; height: 1px; background: var(--line); }
  .address { position: absolute; left: 528px; top: 853px; font-size: 14.5px; line-height: 19px; color: var(--text); font-style: normal; }
</style>
</head>
<body>
<div class="canvas">
  <main class="flyer">
    <div class="hero-photo" role="img" aria-label="Photo of a smiling woman fanning a handful of dollar bills"></div>

    <h1 class="headline">
      <span class="l1">EARN MORTGAGE INCOME</span>
      <span class="l2">IN YOUR SPARE TIME</span>
      <span class="l3">ITS AS EASY AS 1,2,3</span>
    </h1>

    <div class="brand">
      <span class="brand-dot"></span>
      <span class="brand-name">Bluegate Financial Services, Inc.</span>
    </div>

    <section class="steps">
      <div class="step blue" style="left:0;width:262px;">
        <div class="step-num" style="left:76px;">1</div>
        <p>Solicit Potential Applicants (Word of Mouth, Email, Social Media etc.)</p>
      </div>
      <div class="step gold" style="left:270px;width:285px;">
        <div class="step-num" style="left:88px;">2</div>
        <p>Provide us with name, number &amp; email for interested customers</p>
      </div>
      <div class="step blue" style="left:563px;width:220px;">
        <div class="step-num" style="left:62px;">3</div>
        <p>Wait to Get Paid.......(Avg. $2,500 per closing)</p>
      </div>
    </section>

    <div class="family-photo" role="img" aria-label="Faded black and white photo of a happy family"></div>

    <div class="tagline">YOU OPEN THE BLUEGATE, WE'LL HANDLE THE REST</div>

    <ul class="perks">
      <li>No experience necessary</li>
      <li>No goals or quotas for entry level</li>
      <li>No work hours / Work from home</li>
    </ul>

    <p class="reimburse">
      <span class="r1">AND WE FULLY REIMBURSE</span>
      <span class="r2">ALL LICENSING FEES!!</span>
    </p>

    <div class="footer-band"></div>
    <div class="web">www.bluegatehomeloans.com</div>
    <div class="money-bag" role="img" aria-label="Burlap sack overflowing with dollar bills"></div>

    <div class="resume">
      <span class="label">Email Resume to</span>
      <span class="email">mkowal@bluegatehomeloans.com</span>
    </div>

    <div class="contact">
      <p class="call">Call us for more information</p>
      <p class="phone">(800) 640-2915</p>
    </div>
    <div class="rule" style="top:838px;"></div>
    <address class="address">
      Bluegate Financial Services, Inc.<br>
      731 W Orchard Avenue, #318<br>
      Baltimore, MD 21417<br>
      NMLS #386147
    </address>
    <div class="rule" style="top:945px;"></div>
  </main>
</div>
</body>
</html>
```